Business Card Design

Selling Televisions, Velorin, Kavo, Drelvatek, Morenzi
The latest models, sizes ranging from 22"- 75"
Surround Sounds, Sound Bars and Wall Mounts

Target Market(s)

Mainly males/boys/blokes etc

Industry/Entity Type

Business

Contact Information for Business Card

Glen Rudd
07812459306
glrudd@quillnetmail.com

Requirements
Must have
• simplistic design, probably just 2 of the images used

clarity essential
Nice to have
• Metallic if possible

```html
<!DOCTYPE html>
<html lang="en">
<head>
<meta charset="utf-8">
<title>Glen Rudd – Business Card</title>
<link rel="stylesheet" href="https://fonts.googleapis.com/css2?family=Open+Sans:wght@400;600&display=swap">
<style>
  :root {
    --page-bg: #e9e6e1;
    --card-bg: #fbfbfb;
    --ink: #1c1c1c;
    --blue-light: #2aa6dc;
    --blue-dark: #2a6fc4;
    --blue-band: #2c8ed0;
    --orange: #e58a2c;
    --yellow: #f0b322;
    --red: #c8372c;
    --tab-blue: #3569c1;
    --white: #ffffff;
  }
  * { margin: 0; padding: 0; box-sizing: border-box; }
  html, body {
    width: 1200px; height: 900px; overflow: hidden;
    background: var(--page-bg);
    font-family: "Open Sans", Arial, sans-serif;
  }
  .business-card {
    position: absolute; left: 75px; top: 150px;
    width: 1050px; height: 600px;
    background: var(--card-bg);
    border-radius: 6px;
    box-shadow: 0 10px 30px rgba(0,0,0,0.18);
    overflow: hidden;
  }
  .name-header { position: absolute; right: 0; top: 0; width: 520px; height: 150px; }
  .name-header__title {
    position: absolute; right: 60px; top: 30px;
    color: var(--white); font-weight: 600; font-size: 44px; letter-spacing: 0.5px;
  }
  .product-photo {
    position: absolute; left: 50px; top: 175px;
    width: 420px; height: 245px;
    border-radius: 6px;
    background: linear-gradient(135deg, #cfd3da 0%, #a9b4c7 30%, #4f6f9a 60%, #2d3550 100%);
    box-shadow: 0 4px 10px rgba(0,0,0,0.2);
  }
  .services {
    position: absolute; left: 520px; top: 170px; width: 500px;
    text-align: center; color: var(--ink);
    font-size: 27px; line-height: 43px;
  }
  .contact-band {
    position: absolute; left: 0; width: 1050px; height: 62px;
  }
  .contact-band--phone { top: 438px; }
  .contact-band--email { top: 506px; }
  .contact-band__stripe {
    position: absolute; left: 150px; right: 0; top: 0; bottom: 0;
  }
  .contact-band--phone .contact-band__stripe {
    background: linear-gradient(90deg, var(--orange), var(--yellow));
  }
  .contact-band--email .contact-band__stripe {
    background: linear-gradient(90deg, var(--blue-dark), var(--blue-band));
  }
  .contact-band__icon { position: absolute; left: 40px; top: 0; width: 150px; height: 62px; }
  .contact-band__text {
    position: absolute; left: 205px; top: 10px;
    color: var(--white); font-size: 30px; font-weight: 400; letter-spacing: 0.5px;
  }
</style>
</head>
<body>
  <main class="business-card">
    <svg class="name-header" viewBox="0 0 520 150" aria-hidden="true">
      <defs>
        <linearGradient id="headerGradient" x1="0" y1="0" x2="1" y2="0">
          <stop offset="0" stop-color="#2a6fc4"/>
          <stop offset="1" stop-color="#2aa6dc"/>
        </linearGradient>
      </defs>
      <path d="M0 150 C 110 150 150 0 260 0 L520 0 L520 120 L200 120 C 120 120 80 150 0 150 Z" fill="url(#headerGradient)"/>
    </svg>
    <h1 class="name-header__title">Glen Rudd</h1>

    <div class="product-photo" role="img" aria-label="Photo of a wide-screen television showing a city skyline at dusk"></div>

    <p class="services">
      Selling Televisions, Velorin<br>
      Kavo, Drelvatek, Morenzi<br>
      The latest models<br>
      sizes ranging from 22" - 75"<br>
      Surround Sounds<br>
      Sound Bars and Wall Mounts
    </p>

    <div class="contact-band contact-band--phone">
      <div class="contact-band__stripe"></div>
      <svg class="contact-band__icon" viewBox="0 0 150 62" aria-hidden="true">
        <polygon points="0,0 120,0 145,31 120,62 0,62" fill="var(--red)"/>
        <path d="M45 16 c-5 3 -6 9 -2 16 c5 9 11 14 19 15 c4 0 6 -2 7 -5 l-7 -5 l-4 3 c-4 -2 -8 -6 -10 -10 l3 -4 z" fill="var(--white)"/>
      </svg>
      <span class="contact-band__text">07812459306</span>
    </div>

    <div class="contact-band contact-band--email">
      <div class="contact-band__stripe"></div>
      <svg class="contact-band__icon" viewBox="0 0 150 62" aria-hidden="true">
        <polygon points="0,0 120,0 145,31 120,62 0,62" fill="var(--tab-blue)"/>
        <rect x="38" y="17" width="38" height="28" rx="3" fill="none" stroke="var(--white)" stroke-width="3.5"/>
        <path d="M38 19 L57 34 L76 19 M38 44 L51 31 M76 44 L63 31" fill="none" stroke="var(--white)" stroke-width="3.5"/>
      </svg>
      <span class="contact-band__text">glrudd@quillnetmail.com</span>
    </div>
  </main>
</body>
</html>
```